QLDR Individual and Corporate Development Business Card Design

QLDR needs a business card design that is aligned with it's values and targetted markets. Harmonic Ladder of Reasoning Matrix's self diagnosis model and tools, which can be used for personal improvement and team/business performance enhancement, is based on the learnings of over 20 years of medical practitioning. QLDR supercharges personal effectiveness and awareness to also increase team and business performance.

The targetted markets are high performance individuals and teams who aspire seek to enhance their capabilities and achieve their absolute best potential.

Look and feel for the business card design we are looking for is high technology, premium, fresh, new and medical.

Target Market(s)

Industry/Entity Type

Business Consultant

Contact Information for Business Card

Logo, Full Name, Title, Phone number, Email, company name, Address,

Font styles to use
Sans Serif

Requirements
Must have
• Tag line: Maximising Performance for Highly Effective People
• Please use same colours as the logo.

```html
<!DOCTYPE html>
<html lang="en">
<head>
<meta charset="utf-8">
<title>QLDR Business Card</title>
<link href="https://fonts.googleapis.com/css2?family=Open+Sans:wght@400;600;700&display=swap" rel="stylesheet">
<style>
  :root {
    --stage: #1c1c1e;
    --card: #0a0a0b;
    --card-edge: #2a2a2c;
    --teal: #22b8cf;
    --grey-line: #5b6166;
    --white: #f2f4f5;
    --blue-a: #2f7fd0;
    --blue-b: #0a58a8;
  }
  * { box-sizing: border-box; margin: 0; padding: 0; }
  html, body { width: 1200px; height: 900px; overflow: hidden; }
  body {
    background: var(--stage);
    font-family: "Open Sans", Arial, sans-serif;
    position: relative;
  }
  .card {
    position: absolute;
    left: 250px;
    width: 700px;
    height: 400px;
    background: linear-gradient(135deg, #141415 0%, var(--card) 60%);
    border: 1px solid var(--card-edge);
    overflow: hidden;
  }
  .card--front { top: 40px; }
  .card--back { top: 470px; }

  .brand {
    position: absolute;
    display: flex;
    flex-direction: column;
    align-items: flex-start;
  }
  .brand__row { display: flex; align-items: center; gap: 14px; }
  .brand__dot { border-radius: 50%; background: var(--teal); }
  .brand__name {
    color: var(--teal);
    font-weight: 700;
    letter-spacing: 6px;
    line-height: 1;
  }
  .brand__rule { background: var(--grey-line); height: 2px; }
  .brand__full {
    color: var(--teal);
    font-weight: 700;
    text-transform: uppercase;
    letter-spacing: 1.5px;
    line-height: 1.25;
  }

  .card--front .brand { left: 150px; top: 110px; }
  .card--front .brand__dot { width: 26px; height: 26px; }
  .card--front .brand__name { font-size: 96px; }
  .card--front .brand__rule { width: 400px; margin: 14px 0 10px; }
  .card--front .brand__full { font-size: 19px; }

  .card--back .brand { left: 50px; top: 120px; }
  .card--back .brand__dot { width: 16px; height: 16px; }
  .card--back .brand__name { font-size: 58px; letter-spacing: 4px; }
  .card--back .brand__rule { width: 250px; margin: 9px 0 7px; }
  .card--back .brand__full { font-size: 11.5px; letter-spacing: 1px; }

  .divider { position: absolute; left: 0; top: 0; }

  .contact { position: absolute; left: 400px; top: 70px; color: var(--white); }
  .contact__name { font-size: 26px; font-weight: 600; line-height: 1.1; }
  .contact__title { font-size: 14px; color: var(--teal); font-weight: 600; margin-bottom: 44px; }
  .contact__list { list-style: none; font-size: 14px; line-height: 1.6; }
  .contact__item { display: flex; align-items: flex-start; gap: 10px; }
  .contact__item svg { flex: none; margin-top: 4px; }

  .band {
    position: absolute;
    left: 0; bottom: 0;
    width: 100%; height: 70px;
    background: linear-gradient(90deg, var(--blue-a), var(--blue-b));
  }
</style>
</head>
<body>
  <section class="card card--front">
    <div class="brand">
      <div class="brand__row">
        <span class="brand__name">QLDR</span>
        <span class="brand__dot"></span>
      </div>
      <div class="brand__rule"></div>
      <p class="brand__full">Harmonic Ladder<br>of Reasoning Matrix</p>
    </div>
  </section>

  <section class="card card--back">
    <svg class="divider" width="700" height="400" viewBox="0 0 700 400">
      <line x1="330" y1="0" x2="440" y2="330" stroke="#6a6f74" stroke-width="1.2"/>
    </svg>

    <div class="brand">
      <div class="brand__row">
        <span class="brand__name">QLDR</span>
        <span class="brand__dot"></span>
      </div>
      <div class="brand__rule"></div>
      <p class="brand__full">Harmonic Ladder<br>of Reasoning Matrix</p>
    </div>

    <div class="contact">
      <h1 class="contact__name">Your Name</h1>
      <p class="contact__title">Manager</p>
      <ul class="contact__list">
        <li class="contact__item">
          <svg width="14" height="14" viewBox="0 0 24 24"><path fill="#22b8cf" d="M6.6 10.8a15.1 15.1 0 0 0 6.6 6.6l2.2-2.2c.3-.3.7-.4 1-.2 1.1.4 2.3.6 3.6.6.6 0 1 .4 1 1V20c0 .6-.4 1-1 1A17 17 0 0 1 3 4c0-.6.4-1 1-1h3.5c.6 0 1 .4 1 1 0 1.3.2 2.5.6 3.6.1.3 0 .7-.2 1z"/></svg>
          <span>(02) 5550 1234</span>
        </li>
        <li class="contact__item">
          <svg width="14" height="14" viewBox="0 0 24 24"><path fill="#22b8cf" d="M2 5h20v14H2zm2 2v.5l8 5 8-5V7z"/></svg>
          <span>hello@qldr-example.com</span>
        </li>
        <li class="contact__item">
          <svg width="14" height="14" viewBox="0 0 24 24"><path fill="none" stroke="#22b8cf" stroke-width="2.4" d="M12 22s7-7 7-12a7 7 0 0 0-14 0c0 5 7 12 7 12z"/><circle cx="12" cy="10" r="2.5" fill="#22b8cf"/></svg>
          <span>Suite 4, Level 3<br>88 Harbour Lane Northvale</span>
        </li>
      </ul>
    </div>

    <div class="band"></div>
  </section>
</body>
</html>
```